IT Service Provider

We need a website which reflects the IT Services we can offer to small and mid-size companies. This reaches from LAN/WAN, Security, VoIP, WiFi, Storage, Penetration testing.and Support.

In addition to that, a Logo is needed and should be embedded in the website.

Company is registered in the UK under:
Pellwick Ltd
Company No. 05927318

Industry/Entity Type

Security

```html
<!DOCTYPE html>
<html lang="en">
<head>
<meta charset="utf-8">
<title>Pellwick Ltd – IT Services</title>
<link href="https://fonts.googleapis.com/css2?family=Open+Sans:wght@400;600;700&family=Arimo:wght@400;700&display=swap" rel="stylesheet">
<style>
:root{
  --blue:#1a6db5;
  --blue-band:#1b6aa6;
  --navy:#08172a;
  --green:#14a84b;
  --text:#333;
  --muted:#555;
  --line:#bdbdbd;
  --footer:#3b3b3b;
  --footer-outer:#454545;
  --white:#fff;
}
*{box-sizing:border-box;margin:0;padding:0}
html,body{width:970px;height:1200px;overflow:hidden;background:var(--white)}
body{position:relative;font-family:"Arimo",Arial,sans-serif;color:var(--text)}
.abs{position:absolute}
.topline{left:0;top:0;width:970px;height:2px;background:var(--blue)}
.brand{left:144px;top:16px;display:flex;align-items:center;gap:8px}
.brand-mark{width:30px;height:30px;border-radius:50%;background:var(--green)}
.brand-name{font-family:"Open Sans",sans-serif;font-weight:700;font-size:21px;color:var(--green)}
.search{left:530px;top:27px;width:150px;height:21px;border:1px solid #ccc;font-size:9px;font-style:italic;color:#666;padding:5px 6px}
.search svg{position:absolute;right:6px;top:4px}
.callus{left:702px;top:24px;display:flex;gap:6px;align-items:center;font-family:"Open Sans",sans-serif}
.callus small{display:block;font-size:9px;color:#333}
.callus strong{display:block;font-size:16px;font-weight:400;color:#222;line-height:17px}
.nav{left:398px;top:65px;display:flex;font-family:"Open Sans",sans-serif;font-size:11px;font-weight:600;color:#333}
.nav span{padding:0 12px;border-left:1px solid #888;line-height:14px}
.nav span:first-child{border:0;padding-left:0;color:var(--blue)}
.nav span:last-child{padding-right:0}
.hero{left:0;top:96px;width:970px;height:338px;background:var(--navy)}
.hero-photo{left:136px;top:96px;width:698px;height:302px;background:radial-gradient(ellipse at 50% 45%,#7b96e6 0%,#3044a8 40%,#141c5a 75%,#0b1038 100%)}
.hero-arrow{width:30px;height:30px;border-radius:50%;background:rgba(0,0,0,.55);top:238px}
.caption{left:0;top:398px;width:970px;height:36px;background:var(--blue-band);color:var(--white);font-family:"Open Sans",sans-serif;font-size:19px;text-align:center;line-height:36px}
.h2{font-family:"Open Sans",sans-serif;font-weight:600;font-size:17px;color:var(--blue)}
.dash{border-top:1px dashed var(--line);height:0}
.pager{display:flex;gap:10px}
.service{width:140px;text-align:center}
.service h3{font-family:"Open Sans",sans-serif;font-weight:400;font-size:11px;color:#333;margin-bottom:10px}
.service.active h3{color:var(--green);font-weight:600}
.disc{width:98px;height:98px;margin:0 auto;border-radius:50%;background:radial-gradient(circle at 50% 40%,#fafafa,#e2e2e2);border:1px solid #ddd;display:flex;align-items:center;justify-content:center}
.active .disc{border:3px solid var(--green)}
.service p{font-size:9.6px;line-height:14px;margin-top:22px;color:#222}
.rule{left:144px;top:710px;width:690px;height:1px;background:#e6e6e6}
.about-photo{left:144px;top:774px;width:205px;height:94px;background:linear-gradient(90deg,#9fb3c6,#d9c6b6 40%,#3a3e48 70%,#8d9aa8)}
p.body{font-size:9.4px;line-height:12px;color:#333;text-align:justify}
.more{font-size:9px;font-weight:700;color:var(--green)}
.quote{font-size:9.4px;line-height:15px;color:#333}
.quote b{font-family:Georgia,serif;font-size:14px;color:#444}
.who{font-size:8.5px;font-weight:700;color:#555;text-align:right}
.field{left:621px;width:206px;border:1px solid #c9c9c9;border-radius:2px;font-size:8.5px;font-style:italic;color:#666;padding:4px 8px;box-shadow:inset 0 1px 2px rgba(0,0,0,.08)}
.submit{left:622px;top:946px;width:52px;height:18px;background:var(--green);color:var(--white);font-family:"Open Sans",sans-serif;font-weight:600;font-size:10px;text-align:center;line-height:18px}
.client{top:1046px;font-family:"Open Sans",sans-serif;font-weight:700;font-size:17px;color:#555;display:flex;align-items:center;gap:6px}
.client i{display:block;width:14px;height:14px;background:#888}
.footer-outer{left:0;top:1114px;width:970px;height:86px;background:var(--footer-outer)}
.footer{left:136px;top:1114px;width:698px;height:86px;background:var(--footer);color:#eee}
.fnav{left:144px;top:1128px;display:flex;gap:15px;font-size:9px;color:#eee}
.fnav span:first-child{color:var(--green)}
.faddr{left:144px;font-size:8.6px;color:#eee;letter-spacing:.3px}
.connect{left:502px;top:1128px;font-family:"Open Sans",sans-serif;font-size:10px;font-weight:600;color:#fff}
.social{left:502px;top:1154px;display:flex;gap:6px;font-size:8px;color:#ddd}
.social span{display:flex;align-items:center;gap:2px}
.social i{display:block;width:6px;height:6px;background:#4b8ed3}
.flogo{left:712px;top:1128px;display:flex;align-items:center;gap:5px;font-family:"Open Sans",sans-serif;font-weight:700;font-size:16px;color:#8a8a8a}
.flogo i{display:block;width:18px;height:18px;border-radius:50%;background:#8a8a8a}
.copy{left:663px;top:1171px;font-size:8.6px;color:#eee}
</style>
</head>
<body>
<div class="abs topline"></div>

<header>
  <div class="abs brand"><span class="brand-mark"></span><span class="brand-name">Pellwick Ltd</span></div>
  <div class="abs search">search
    <svg width="11" height="11" viewBox="0 0 11 11"><circle cx="4.5" cy="4.5" r="3.5" fill="none" stroke="#888" stroke-width="1.3"/><line x1="7" y1="7" x2="10" y2="10" stroke="#888" stroke-width="1.5"/></svg>
  </div>
  <div class="abs callus">
    <svg width="26" height="26" viewBox="0 0 26 26"><circle cx="13" cy="13" r="11.5" fill="none" stroke="#14a84b" stroke-width="1.6"/><path d="M10 7c-1 1-2 3 0 7s4 6 6 5l1-1-2-3-2 1c-1-1-2-3-2-4l2-1-1-3z" fill="#14a84b"/></svg>
    <div><small>Call Us Today</small><strong>123 555 0148</strong></div>
  </div>
  <nav class="abs nav"><span>HOME</span><span>ABOUT US</span><span>SERVICES</span><span>TESTIMONIALS</span><span>CLIENTS</span><span>CONTACT US</span></nav>
</header>

<section>
  <div class="abs hero"></div>
  <div class="abs hero-photo" role="img" aria-label="Server room corridor lit in blue"></div>
  <div class="abs hero-arrow" style="left:145px"><svg width="30" height="30"><path d="M17 9l-6 6 6 6" fill="none" stroke="#fff" stroke-width="1.5"/></svg></div>
  <div class="abs hero-arrow" style="left:795px"><svg width="30" height="30"><path d="M13 9l6 6-6 6" fill="none" stroke="#fff" stroke-width="1.5"/></svg></div>
  <div class="abs caption">WE HAVE SPECIALISED ENGINEERS TO DO SPECIALISED WORK</div>
</section>

<section>
  <h2 class="abs h2" style="left:146px;top:466px">Our Services</h2>
  <div class="abs dash" style="left:144px;top:490px;width:688px"></div>
  <div class="abs pager" style="left:798px;top:474px">
    <svg width="8" height="12"><path d="M7 1L2 6l5 5" fill="none" stroke="#666" stroke-width="1.3"/></svg>
    <svg width="8" height="12"><path d="M1 1l5 5-5 5" fill="none" stroke="#14a84b" stroke-width="1.3"/></svg>
  </div>

  <div class="abs service active" style="left:132px;top:512px"><h3>Lanwan</h3>
    <div class="disc"><svg width="50" height="46" viewBox="0 0 50 46" fill="none" stroke="#555" stroke-width="4"><rect x="19" y="2" width="12" height="10"/><path d="M25 12v10M8 22h34M8 22v8M42 22v8"/><rect x="2" y="31" width="12" height="10"/><rect x="36" y="31" width="12" height="10"/></svg></div>
    <p>Lorem ipsum dolor sit amet ummy nibh eui smod</p></div>
  <div class="abs service" style="left:272px;top:512px"><h3>Security</h3>
    <div class="disc"><svg width="40" height="46" viewBox="0 0 40 46"><path d="M20 2L3 8v14c0 11 8 19 17 22 9-3 17-11 17-22V8z" fill="none" stroke="#555" stroke-width="4"/><path d="M20 9l-10 4v8c0 7 5 12 10 14z" fill="#555"/></svg></div>
    <p>Lorem ipsum dolor sit amet ummy nibh eui smod</p></div>
  <div class="abs service" style="left:414px;top:512px"><h3>VoIP</h3>
    <div class="disc"><svg width="56" height="40" viewBox="0 0 56 40" fill="#555"><path d="M4 14c0-8 48-8 48 0v4h-12v-5c-6-2-18-2-24 0v5H4z"/><path d="M14 20h28l8 18H6z"/><circle cx="28" cy="28" r="5" fill="#e8e8e8"/></svg></div>
    <p>Lorem ipsum dolor sit amet ummy nibh eui smod</p></div>
  <div class="abs service" style="left:555px;top:512px"><h3>WiFi</h3>
    <div class="disc"><svg width="52" height="40" viewBox="0 0 52 40" fill="none" stroke="#555" stroke-width="5" stroke-linecap="round"><path d="M4 14c13-12 31-12 44 0"/><path d="M12 22c8-7 20-7 28 0"/><path d="M20 30c3-3 9-3 12 0"/><circle cx="26" cy="36" r="1.5" fill="#555"/></svg></div>
    <p>Lorem ipsum dolor sit amet ummy nibh eui smod</p></div>
  <div class="abs service" style="left:696px;top:512px"><h3>Storage</h3>
    <div class="disc"><svg width="46" height="50" viewBox="0 0 46 50" fill="#555"><ellipse cx="23" cy="8" rx="21" ry="7"/><path d="M2 12c4 5 38 5 42 0v9c-4 6-38 6-42 0z"/><path d="M2 25c4 5 38 5 42 0v9c-4 6-38 6-42 0z"/><path d="M2 38c4 5 38 5 42 0v4c0 4-9 7-21 7S2 46 2 42z"/></svg></div>
    <p>Lorem ipsum dolor sit amet ummy nibh eui smod</p></div>
</section>

<div class="abs rule"></div>

<section>
  <h2 class="abs h2" style="left:144px;top:740px">About Pellwick Ltd</h2>
  <div class="abs dash" style="left:144px;top:764px;width:206px"></div>
  <div class="abs about-photo" role="img" aria-label="Team of consultants meeting around a desk"></div>
  <p class="abs body" style="left:144px;top:875px;width:204px">Lorem Nonummy nibh uismod tincidunt ut laoreet olore magna aliquam erat volutpat. Ut wisi enim adinim nonummy nibh euismod tincidunt Nonummy nibh uismod tincidunt ut laoreet dolore magna aliquam erat volutpat. Ut wdreisi enim ad adinim nonummy nibh euismod tincidun Lorem Nonummy.</p>
  <div class="abs more" style="left:294px;top:956px">Read More »</div>

  <h2 class="abs h2" style="left:380px;top:740px">Client Testimonials</h2>
  <div class="abs dash" style="left:380px;top:764px;width:208px"></div>
  <p class="abs quote" style="left:377px;top:778px;width:216px"><b>“</b> Nonummy nibh uismod tincidunt ut laoreet dolore magna aliquam erat volutpat. Ut wisi enim ad minim nonummy nibh euismod tincidunt <b>”</b></p>
  <div class="abs who" style="left:440px;top:823px;width:150px">Daniel Marsh</div>
  <p class="abs quote" style="left:377px;top:845px;width:216px"><b>“</b> Nonummy nibh uismod tincidunt ut laoreet olore magna aliquam erat volutpat. Ut wisi enim adinim nonummy nibh euismod tincidunt Nonummy nibh uismod tincidunt ut laoreet dolore magna aliquam erat volutpat. Ut wisi enim ad minim nonummy nibh lorem tincidunt <b>”</b></p>
  <div class="abs who" style="left:440px;top:933px;width:150px">Owen Pryce</div>
  <div class="abs more" style="left:539px;top:956px">Read More »</div>

  <h2 class="abs h2" style="left:619px;top:740px">Quick Contact</h2>
  <div class="abs dash" style="left:619px;top:764px;width:209px"></div>
  <div class="abs field" style="top:774px;height:22px">Name</div>
  <div class="abs field" style="top:807px;height:22px">Email</div>
  <div class="abs field" style="top:840px;height:22px">Phone</div>
  <div class="abs field" style="top:872px;height:62px">Message</div>
  <div class="abs submit">Submit</div>
</section>

<section>
  <h2 class="abs h2" style="left:143px;top:997px">Our Clients</h2>
  <div class="abs dash" style="left:143px;top:1022px;width:689px"></div>
  <div class="abs pager" style="left:798px;top:1004px">
    <svg width="8" height="12"><path d="M7 1L2 6l5 5" fill="none" stroke="#666" stroke-width="1.3"/></svg>
    <svg width="8" height="12"><path d="M1 1l5 5-5 5" fill="none" stroke="#14a84b" stroke-width="1.3"/></svg>
  </div>
  <div class="abs client" style="left:143px"><i></i>Northvane</div>
  <div class="abs client" style="left:284px">Corelith</div>
  <div class="abs client" style="left:430px">Quantra</div>
  <div class="abs client" style="left:525px">Bexwell</div>
  <div class="abs client" style="left:620px">Corelith</div>
  <div class="abs client" style="left:762px">Quantra</div>
</section>

<footer>
  <div class="abs footer-outer"></div>
  <div class="abs footer"></div>
  <div class="abs fnav"><span>Home</span><span>About Us</span><span>Services</span><span>Testimonials</span><span>Clients</span><span>Contact Us</span></div>
  <div class="abs faddr" style="top:1156px">Street Name, City Name State Zip code</div>
  <div class="abs faddr" style="top:1172px">☎ 123-555-0148 &nbsp; ✉ inquiry@pellwick.co.uk</div>
  <div class="abs connect">Connect Us On</div>
  <div class="abs social"><span><i></i>Socialia</span><span><i></i>Postwire</span><span><i></i>Workfeed</span><span><i style="background:#e8862a"></i>Newsline</span></div>
  <div class="abs flogo"><i></i>Pellwick</div>
  <div class="abs copy">© 2014 Pellwick Ltd. All Rights Reserved · Co. No. 05927318</div>
</footer>
</body>
</html>
```